Business card design needed

We need a business card design for our new company KiraVelle Event Creations, based in Leeton NSW. We will however be serving the whole Riverina area. We plan any events like, Parties, Weddings ext. We would like to see designs that is vibrant but elegant. Mainly we would like to have our Name displayed on the front and all the other info at the back. We need a design that will catch the eye anywhere.Design FRONT AND BACK
Updates

Industry/Entity Type

Events

Contact Information for Business Card

KiraVelle Event Creations
Tessa Verhulst

0461593802
kiravelle@brightmail.example

Believe the Impossible

Requirements
Must have
• Elegant Coulors and Fonts

```html
<!DOCTYPE html>
<html lang="en">
<head>
<meta charset="utf-8">
<title>KiraVelle Event Creations – Business Card</title>
<link rel="stylesheet" href="https://fonts.googleapis.com/css2?family=Syncopate:wght@400;700&family=Quicksand:wght@600&display=swap">
<style>
  :root {
    --stage: #e9e6e1;
    --card: #2d2d2e;
    --card-deep: #242425;
    --green: #5db936;
    --green-band: #58b032;
    --ink: #121212;
    --light: #ecebe8;
    --icon: #1c1c1c;
  }
  * { margin: 0; padding: 0; box-sizing: border-box; }
  html, body { width: 1200px; height: 800px; overflow: hidden; }
  body {
    background: var(--stage);
    display: flex;
    align-items: center;
    justify-content: center;
    gap: 40px;
  }
  .card {
    position: relative;
    width: 540px;
    height: 309px;
    border-radius: 4px;
    overflow: hidden;
    box-shadow: 0 10px 28px rgba(0,0,0,.28);
  }
  .card-texture {
    position: absolute;
    inset: 0;
    background: radial-gradient(ellipse at 50% 40%, var(--card) 0%, var(--card-deep) 100%);
  }

  /* Front */
  .front-brand {
    position: absolute;
    left: 0; right: 0;
    top: 108px;
    text-align: center;
    font-family: "Syncopate", sans-serif;
    font-weight: 700;
    color: var(--green);
  }
  .front-brand .brand-name { display: block; font-size: 34px; letter-spacing: 2px; line-height: 1; }
  .front-brand .brand-rule {
    display: block;
    width: 330px;
    height: 2px;
    margin: 12px auto 10px;
    background: var(--green);
  }
  .front-brand .brand-sub { display: block; font-size: 15px; letter-spacing: 2px; line-height: 1; }

  /* Back */
  .back-company {
    position: absolute;
    right: 40px;
    top: 98px;
    font-family: "Syncopate", sans-serif;
    font-weight: 700;
    font-size: 13px;
    letter-spacing: 3px;
    color: var(--green);
    z-index: 2;
  }
  .tagline-band {
    position: absolute;
    left: 0; right: 0;
    top: 118px;
    height: 58px;
    background: var(--green-band);
    display: flex;
    align-items: center;
    justify-content: center;
  }
  .tagline {
    font-family: "Quicksand", sans-serif;
    font-weight: 600;
    font-size: 21px;
    color: var(--ink);
    letter-spacing: .3px;
    padding-top: 8px;
  }
  .contact {
    position: absolute;
    left: 72px;
    top: 194px;
    font-family: "Syncopate", sans-serif;
    color: var(--light);
  }
  .contact-name { font-size: 15px; font-weight: 700; letter-spacing: 3px; margin-bottom: 10px; }
  .contact-line {
    display: flex;
    align-items: center;
    gap: 12px;
    font-size: 11px;
    letter-spacing: 2px;
    height: 28px;
  }
  .contact-line svg { width: 22px; height: 18px; flex: none; }
</style>
</head>
<body>

<section class="card card-front" aria-label="Business card front">
  <div class="card-texture" role="img" aria-label="Dark charcoal card stock with a subtle embossed damask pattern"></div>
  <h1 class="front-brand">
    <span class="brand-name">KiraVelle</span>
    <span class="brand-rule"></span>
    <span class="brand-sub">Event Creations</span>
  </h1>
</section>

<section class="card card-back" aria-label="Business card back">
  <div class="card-texture" role="img" aria-label="Dark charcoal card stock with a subtle embossed damask pattern"></div>
  <p class="back-company">KiraVelle Event Creations</p>
  <div class="tagline-band">
    <p class="tagline">Believe the Impossible</p>
  </div>
  <div class="contact">
    <p class="contact-name">Tessa Verhulst</p>
    <p class="contact-line">
      <svg viewBox="0 0 22 18" aria-hidden="true">
        <path d="M4 2 C2 3 1 5 3 9 C5 13 9 16 13 16 C15 16 16 15 17 14 L14 11 L12 12.5 C10 12 7 9 6.5 7 L8 5 Z" fill="var(--icon)" stroke="#555" stroke-width=".8"/>
      </svg>
      <span>0461593802</span>
    </p>
    <p class="contact-line">
      <svg viewBox="0 0 22 18" aria-hidden="true">
        <rect x="1.5" y="3" width="19" height="13" rx="1.5" fill="var(--icon)" stroke="#555" stroke-width=".8"/>
        <path d="M1.5 3.5 L11 10.5 L20.5 3.5" fill="none" stroke="#555" stroke-width=".9"/>
      </svg>
      <span>kiravelle@brightmail.example</span>
    </p>
  </div>
</section>

</body>
</html>
```